Wordpress Design Project (Brookmere)

We need a wordpress design for an established auction and real estate company based in New Hampshire. The winning design will incorporate the colors of logo (red and blue) creatively with black or gray in a very professional and clean layout. Client mentions liking the site http://www.tarvellauction.com/ as a general idea.

Industry/Entity Type

Real Estate

Requirements
Must have
• Navigation:
1) Home (lorem text)
2) Upcoming Auctions
3) Auction Results
4) Sell or Consign
5) About Us
6) Services
7) FAQ
8) Contact Us

Site will have slideshow, initial image attached.
Sidebar widgets:
- Email sign up form
- Featured Auction (like at http://www.pinderauctionco.com) - - - - Video Widget
- Testimonials widget

Footer will have smaller logo, contact info, and 2 association logos (attached)
-
Nice to have
• use of drop-down menu design for 'Services'
1) Appraisals
2) Consulting
Should not have
• please use no gavels in the design

```html
<!DOCTYPE html>
<html lang="en">
<head>
<meta charset="utf-8">
<title>Brookmere Auctioneers</title>
<link rel="stylesheet" href="https://fonts.googleapis.com/css2?family=Open+Sans:wght@400;600;700&family=Oswald:wght@600;700&family=Teko:wght@600&family=Roboto:ital,wght@0,400;0,700;1,400;1,700&display=swap">
<style>
:root{
  --navy:#14235e;
  --navy-deep:#0b1542;
  --red:#a3000b;
  --ink:#333;
  --footer:#2a2a2a;
}
*{box-sizing:border-box;margin:0;padding:0}
html,body{width:920px;height:1200px;overflow:hidden}
body{background:linear-gradient(180deg,#0c1a55 0%,#1c2f84 70%,#162872 100%);font-family:"Roboto",Arial,sans-serif;color:var(--ink);position:relative}
.page{position:absolute;left:53px;top:9px;width:815px;height:1191px;background:linear-gradient(180deg,#fff 0%,#f6f6f7 60%,#eee 100%)}
.abs{position:absolute}
.brand{left:35px;top:20px;display:flex;align-items:center;gap:10px}
.brand .dot{width:58px;height:58px;border-radius:50%;background:var(--navy)}
.brand span{font-family:"Open Sans",sans-serif;font-size:30px;color:var(--navy);letter-spacing:1px}
.phone-tab{left:499px;top:0;width:248px;height:41px;background:var(--navy-deep);border-radius:0 0 30px 30px;display:flex;align-items:center;justify-content:center;gap:9px;white-space:nowrap}
.phone-tab .ic{width:26px;height:26px;border-radius:50%;background:#3c63b5;border:2px solid #c9d6f2;flex:none}
.phone-tab b{font-family:"Teko",sans-serif;font-size:25px;color:#fff;letter-spacing:1px;line-height:1;padding-top:4px}
.social{left:553px;top:67px;display:flex;gap:16px}
.social i{width:16px;height:16px;border-radius:3px;background:#5a6a96;display:block}
.nav{left:3px;top:109px;width:808px;height:47px;background:linear-gradient(180deg,#233a8a,#101d57);border-radius:24px;display:flex;overflow:hidden}
.nav a{font-family:"Open Sans",sans-serif;font-size:10px;color:#fff;text-decoration:none;display:flex;align-items:center;justify-content:center;border-right:1px solid #2c428f;height:100%;white-space:nowrap;flex:none}
.nav a:last-child{border:0}
.nav a.on{background:var(--red)}
.drop{left:474px;top:156px;width:128px;background:var(--navy)}
.drop div{font-family:"Open Sans",sans-serif;font-size:10px;color:#fff;height:29px;display:flex;align-items:center;padding-left:18px;position:relative}
.drop div:first-child{background:var(--red)}
.drop div::before{content:"";position:absolute;left:8px;top:11px;border:3px solid transparent;border-left:4px solid #fff}
.slider{left:10px;top:163px;width:796px;height:342px;background:#fff;box-shadow:0 1px 4px rgba(0,0,0,.15)}
.slide-photo{left:10px;top:10px;width:660px;height:320px;background:linear-gradient(135deg,#6c5a3e,#b9a57a 45%,#3e3424)}
.signup-art{left:0;top:0}
.signup-title{left:640px;top:184px;width:132px;text-align:right;color:#fff;font-family:"Teko",sans-serif;font-size:44px;line-height:.85}
.signup-sub{left:640px;top:222px;width:127px;text-align:right;color:#fff;font-family:"Teko",sans-serif;font-size:18px;letter-spacing:1px;line-height:1}
.signup-text{left:574px;top:262px;width:228px;color:#fff;font-family:"Open Sans",sans-serif;font-size:10px;line-height:14.5px}
.field{left:578px;width:219px;height:32px;border:1px solid #d4363e;border-radius:14px;background:#8d0008;font-family:"Open Sans",sans-serif;font-size:10px;font-weight:600;color:#f1c9cb;padding:9px 12px}
.btn-sign{left:705px;top:414px;width:88px;height:23px;border:1px solid #d4363e;border-radius:5px;color:#fff;font-family:"Open Sans",sans-serif;font-size:9px;font-weight:700;display:flex;align-items:center;justify-content:center}
.welcome{left:0;top:541px;width:815px;text-align:center;font-family:"Open Sans",sans-serif;font-size:19px;font-weight:600;color:var(--navy)}
.welcome em{font-style:normal;color:var(--red)}
.intro{left:20px;top:586px;width:775px;text-align:center;font-size:10px;line-height:16px;color:#444}
.rule{left:20px;top:688px;width:775px;height:2px;background:linear-gradient(90deg,transparent,#ddd,transparent)}
.sect{font-family:"Oswald",sans-serif;font-size:19px;font-weight:700;color:#333;line-height:1}
.sect em{font-style:normal;color:var(--red)}
.list{left:9px;top:733px;width:540px;height:345px;background:#f7f7f7}
.item{position:absolute;left:12px;width:522px;height:111px;border-bottom:1px dashed #ccc}
.thumb{position:absolute;left:6px;top:0;width:110px;height:75px;border:2px solid #d3d3d3}
.info{position:absolute;left:126px;top:-1px;font-size:9.3px;font-style:italic;color:#333;line-height:11px}
.info h5{font-size:11.5px;color:var(--red);font-weight:400;margin-bottom:6px}
.info b{margin-right:3px}
.info .loc{margin-top:11px}
.pill{position:absolute;left:421px;width:87px;height:18px;border-radius:9px;font-family:"Open Sans",sans-serif;font-size:9.5px;font-weight:700;color:#fff;display:flex;align-items:center;justify-content:center;letter-spacing:.5px;border:1px solid #555}
.pill.red{background:linear-gradient(#d8222c,#9c000a)}
.pill.dark{background:linear-gradient(#555,#111)}
.more{left:440px;top:1066px;width:70px;height:16px;background:#eee;border-radius:8px 8px 0 0;font-size:8.5px;font-weight:700;color:var(--navy);text-align:center;line-height:16px}
.video{left:580px;top:733px;width:212px;height:164px;border-radius:18px;background:#ddd}
.video-still{left:590px;top:743px;width:192px;height:144px;border-radius:14px;background:linear-gradient(135deg,#b59a6c,#e0d5c0 50%,#a55 100%)}
.play{left:662px;top:790px;width:50px;height:50px;border-radius:50%;border:3px solid rgba(255,255,255,.8);background:rgba(255,255,255,.25)}
.play::after{content:"";position:absolute;left:17px;top:12px;border:11px solid transparent;border-left:16px solid rgba(255,255,255,.9)}
.quote{left:586px;top:963px;width:193px;height:78px;background:#eee;border:1px solid #ccc;font-size:9.8px;line-height:14.5px;padding:7px 9px;color:#222}
.tail{left:700px;top:1040px}
.by{left:681px;top:1066px;font-size:9.5px;line-height:14.5px;color:#333}
.avatar{left:750px;top:1061px;width:27px;height:27px;background:linear-gradient(#8a6a56,#d8b9a2)}
.footer{left:0;top:1122px;width:815px;height:69px;background:var(--footer);color:#ddd;font-size:8.8px;line-height:18px;padding:9px 18px}
.f-brand{left:482px;top:1142px;display:flex;align-items:center;gap:5px}
.f-brand .dot{width:30px;height:30px;border-radius:50%;background:#cfd4dd}
.f-brand span{font-family:"Open Sans",sans-serif;font-size:13px;color:#ddd;letter-spacing:.5px}
.badge{top:1146px;background:#ddd}
</style>
</head>
<body>
<div class="page">
  <div class="abs brand"><div class="dot"></div><span>BROOKMERE</span></div>
  <div class="abs phone-tab"><div class="ic"></div><b>(555) 014 2290</b></div>
  <div class="abs social"><i></i><i></i><i></i><i></i><i></i></div>

  <nav class="abs nav">
    <a style="width:78px;padding-left:8px">HOME</a><a style="width:147px">UPCOMING AUCTIONS</a><a style="width:124px">AUCTION RESULTS</a><a style="width:122px">SELL OR CONSIGN</a><a class="on" style="width:83px">SERVICES</a><a style="width:83px">ABOUT US</a><a style="width:61px">FAQ</a><a style="width:110px;padding-right:8px">CONTACT US</a>
  </nav>

  <div class="abs slider">
    <div class="abs slide-photo" role="img" aria-label="Trays of graded coins in protective holders"></div>
    <svg class="abs signup-art" width="796" height="342" viewBox="0 0 796 342">
      <defs><clipPath id="c"><rect x="10" y="10" width="775" height="322"/></clipPath></defs>
      <g clip-path="url(#c)">
        <circle cx="702" cy="172" r="188" fill="#fff"/>
        <circle cx="704" cy="172" r="174" fill="#a3000b"/>
      </g>
    </svg>
  </div>
  <div class="abs drop"><div>APPRAISALS</div><div>CONSULTING</div></div>

  <div class="abs signup-title">EMAIL</div>
  <div class="abs signup-sub">SIGNUP</div>
  <p class="abs signup-text">Pellentesque habitant morbi tristique senectus et netus et malesuada fames ac turpis egestas. In posuere felis nec tortor.</p>
  <div class="abs field" style="top:314px">Your Name</div>
  <div class="abs field" style="top:358px">Your Email</div>
  <div class="abs btn-sign">Sign Up Now</div>

  <h2 class="abs welcome">Welcome To <em>BROOKMERE</em></h2>
  <p class="abs intro"><b><i>simply dummy text of the printing and typesetting industry. Lorem Ipsum has been the industry's standard dummy text ever since the 1500s, when an</i></b> unknown printer took a galley of type and scrambled it to make a type speci men book. It has survived not only five centuries, but also a galley of type and scrambled&nbsp; the leap into electronic typesetting, remaining essen tially unchanged. It was popularised in the 1960s with the release of Letraset sheets containing Lorem Ipsum passages.<b>but also a galley of type and scrambled&nbsp; the leap into electronic</b> typesetting, remaining essen tially unchanged. It was popularised in the 1960s with the release of Letraset sheets containing Lorem Ipsum passages.</p>
  <div class="abs rule"></div>

  <h2 class="abs sect" style="left:11px;top:704px"><em>Upcoming</em> Auctions</h2>
  <div class="abs" style="left:175px;top:714px;width:370px;height:3px;background:#ddd"></div>
  <div class="abs list">
    <div class="item" style="top:10px">
      <div class="thumb" role="img" aria-label="Stack of coins" style="background:linear-gradient(#e8e4dc,#b9a88a)"></div>
      <div class="info"><h5>Live On-site Auction With Online Bidding</h5><b>Begins:</b> Tuesday, April 23, 2013 at 10:00 AM EDT<div class="loc"><b>Location:</b> Willow Ridge Entrance- 1800 N. Valley Rd 14<br>Willow Ridge Rd (Auction Property)<br>Ashford, NH 03601</div></div>
      <div class="pill red" style="top:5px">DETAILS</div><div class="pill dark" style="top:34px">PHOTOS</div>
    </div>
    <div class="item" style="top:121px">
      <div class="thumb" role="img" aria-label="Gold coins" style="background:radial-gradient(circle at 35% 50%,#e0b44a,#7a4a0e 70%,#2a1a08)"></div>
      <div class="info"><h5>Live On-site Auction With Online Bidding</h5><b>Begins:</b> Tuesday, April 23, 2013 at 10:00 AM EDT<div class="loc"><b>Location:</b> Willow Ridge Entrance- 1800 N. Valley Rd 14<br>Willow Ridge Rd (Auction Property)<br>Ashford, NH 03601</div></div>
      <div class="pill red" style="top:4px">DETAILS</div><div class="pill dark" style="top:31px">PHOTOS</div>
    </div>
    <div class="item" style="top:233px">
      <div class="thumb" role="img" aria-label="Silver coins" style="background:radial-gradient(circle,#c9c9c9,#555 55%,#111)"></div>
      <div class="info"><h5>Live On-site Auction With Online Bidding</h5><b>Begins:</b> Tuesday, April 23, 2013 at 10:00 AM EDT<div class="loc"><b>Location:</b> Willow Ridge Entrance- 1800 N. Valley Rd 14<br>Willow Ridge Rd (Auction Property)<br>Ashford, NH 03601</div></div>
      <div class="pill red" style="top:3px;left:424px">DETAILS</div><div class="pill dark" style="top:31px;left:424px">PHOTOS</div>
    </div>
  </div>
  <div class="abs more">more info[+]</div>

  <h2 class="abs sect" style="left:594px;top:704px"><em>Featured</em> Auction</h2>
  <div class="abs video"></div>
  <div class="abs video-still" role="img" aria-label="Video of an auctioneer presenting to a crowd"></div>
  <div class="abs play"></div>

  <h2 class="abs sect" style="left:594px;top:930px"><em>Recent</em> Testimonial</h2>
  <div class="abs quote">Simply dummy text of the printing and typesetting industry. Lorem Ipsum has been the industry's standard dummy text ever since the 1500s,</div>
  <svg class="abs tail" width="30" height="22" viewBox="0 0 30 22"><path d="M0 0 L20 20 L20 0" fill="#eee" stroke="#ccc"/><rect x="1" y="0" width="18" height="2" fill="#eee"/></svg>
  <div class="abs by">By<br>Lena Hartwell</div>
  <div class="abs avatar" role="img" aria-label="Client portrait"></div>

  <footer class="abs footer">Brookmere Auctioneers<br>48 Alder Lane • Ashford, NH 03601<br>P: 555-014-7721 • F: 555-014-7722 • info@BrookmereAuctioneers.com</footer>
  <div class="abs f-brand"><div class="dot"></div><span>BROOKMERE</span></div>
  <div class="abs badge" style="left:619px;width:33px;height:28px"></div>
  <div class="abs badge" style="left:677px;width:115px;height:28px"></div>
</div>
</body>
</html>
```